Pale Lantern Double Sided Flyer Design

We need a double sided flyer (1/3 of an A4 which is 99mm x 210mm) developed for our Newcastle(NSW) tour. This flyer will be placed in tourist information centres and hotels. We want it to direct people to our website or be able to make bookings over the phone.

About Us:-
We are a city walking tour company that runs tours day or night. We run both day and night and will incorporate real history / real Pale lantern. Some of the stories will be quite serious i.e.- there are infamous murders from 100 years ago, baffling court cases, even a bit of poetry written by murderers, suicides, love triangles, you name it. We will be telling the historical stories that tourists will not hear from any other tour provider. A bit of darkness, a bit of mystery and a bit of history theme.

We do no go for scares and let the very real stories deliver the entertainment for our guests. Our customers enjoy our tours, but it isn't light fun and frivolity. Our stories are being carefully crafted and are packed with unexpected twists, turns; revelations whilst remaining all 100% true. We deliver deep, rich, engaging stories.

Here are a few samples of quotes from the characters in our stories that may give you an idea of the kind of history we will cover:-

"There were bits of spines, bits of skulls, [and] finger bones spilled out all over the streets - I ended up filling three boxes. Children were playing with them for weeks”

"I had a close shave last night and now I want a close haircut.”

“She's a beautiful child', isn't she? She's the cause of all the trouble.”

“I did it because she would not come home with me.”

"I have killed my wife. I’m glad she’s dead.”

"Stand aside or I'll put a bullet through both of you."

“You villain, I'll teach you to take away my character."

“You’re not dead yet, you bastard!”

Our website, booking form and contact details can be viewed at www.palelantern.com.au

Target Market(s)

Tourists

Industry/Entity Type

Tour

Colors

Designer to choose colors to be used in the design.

Requirements
Must have
• Vertical orientation please.
• Please also include a reference to a discount offer of 25% using the promo code "WICK".
Nice to have
• FRONT FLYER INFORMATION
• - Pale Lantern Logo
• - "I have killed my wife; I'm glad she's dead."
• - Harbourside Hidden Lanes Walk
• - 25% Discount Offer Codeword WICK
• - web address at the base; www.palelantern.com.au
• BACK FLYER INFORMATION
• - "She's a beautiful child', isn't she? She's the cause of all the trouble.
• - Pale Lantern Logo at the base along with the web address www.palelantern.com.au
• - Blurb:- Pale lantern brings back Newcastle's hidden past, the forgotten past, the dark past that may not want to be remembered.
• Real stories from the streets around you. Discover the histories you won't hear anywhere else. The forgotten stories of yesteryear finally get a chance to be told. Through you they get to live again.
Should not have
• GENERAL
• Please do not include the phone number, email address or social media icons. We want to drive online bookings.

```html
<!DOCTYPE html>
<html lang="en">
<head>
<meta charset="utf-8">
<title>Pale Lantern – Harbourside Hidden Lanes Walk Flyer</title>
<link href="https://fonts.googleapis.com/css2?family=Rye&family=Open+Sans:wght@400;600;700;800&family=Montserrat:wght@500;700&display=swap" rel="stylesheet">
<style>
  :root{
    --page:#ffffff;
    --sepia-light:#c79a5a;
    --sepia-mid:#8a4a22;
    --rust:#6b2a14;
    --night:#0d0705;
    --quote-yellow:#f8d43c;
    --quote-edge:#a3201a;
    --ribbon:#c8251d;
    --ribbon-dark:#7e120e;
    --ink-white:#ffffff;
    --logo-red:#c8251d;
    --rule:#8c7a6a;
  }
  *{margin:0;padding:0;box-sizing:border-box}
  html,body{width:1177px;height:1200px;overflow:hidden;background:var(--page)}
  body{position:relative;font-family:"Open Sans",Arial,sans-serif}

  .flyer-side{position:absolute;top:34px;width:528px;height:1120px;overflow:hidden;background:var(--night)}
  .flyer-side--front{left:38px}
  .flyer-side--back{left:604px}

  .scene-art{position:absolute;inset:0}
  .flyer-side--front .scene-art{
    background:
      linear-gradient(to bottom, rgba(13,7,5,0) 55%, rgba(13,7,5,.85) 75%, var(--night) 88%),
      radial-gradient(ellipse at 60% 35%, var(--sepia-light) 0%, var(--sepia-mid) 45%, var(--rust) 80%);
  }
  .flyer-side--back .scene-art{
    background:
      linear-gradient(to bottom, rgba(13,7,5,0) 55%, rgba(13,7,5,.9) 78%, var(--night) 90%),
      radial-gradient(ellipse at 45% 30%, #b07a44 0%, var(--sepia-mid) 45%, #4a1c0c 85%);
  }

  .brand-box{position:absolute;left:151px;top:38px;width:226px;height:126px;background:var(--ink-white);
    display:flex;align-items:center;justify-content:center;gap:10px}
  .brand-name{font-family:"Open Sans",Arial,sans-serif;font-weight:800;font-size:25px;color:var(--logo-red);letter-spacing:.5px}
  .brand-mark{width:16px;height:16px;background:var(--logo-red)}

  .quote{position:absolute;left:0;right:0;font-family:"Rye",Georgia,serif;color:var(--quote-yellow);
    text-shadow:2px 2px 0 var(--quote-edge),-1px -1px 0 var(--quote-edge),1px -1px 0 var(--quote-edge),-1px 1px 0 var(--quote-edge),4px 4px 6px rgba(0,0,0,.5);
    line-height:1.05;text-transform:uppercase}
  .quote .line{display:block}
  .quote .mark{font-size:1.3em;color:var(--ink-white);text-shadow:none;vertical-align:-.15em}
  .quote .big{font-size:1.6em}

  .quote--front{top:211px;padding-left:62px;font-size:44px}
  .quote--back{top:51px;padding:0 40px;font-size:40px;text-align:right}

  .tour-title{position:absolute;left:0;right:0;top:795px;text-align:center;color:var(--ink-white);font-family:"Montserrat",Arial,sans-serif}
  .tour-title__place{display:block;font-size:30px;font-weight:500;letter-spacing:6px}
  .tour-title__name{display:block;font-size:60px;font-weight:700;line-height:1.05;letter-spacing:1px}

  .ribbon{position:absolute}
  .ribbon svg{position:absolute;inset:0;width:100%;height:100%}
  .ribbon__text{position:relative;height:100%;display:flex;flex-direction:column;align-items:center;justify-content:center;color:var(--ink-white);text-align:center}

  .ribbon--walk{left:56px;top:886px;width:406px;height:40px}
  .ribbon--walk .ribbon__text{font-family:"Montserrat",Arial,sans-serif;font-weight:700;font-size:26px;letter-spacing:5px}

  .ribbon--offer{left:122px;top:946px;width:293px;height:85px}
  .offer-amount{font-size:26px;font-weight:800;color:#ffe680;line-height:1.1}
  .offer-code{font-size:17px;font-weight:600}

  .ribbon--blurb{left:60px;top:616px;width:400px;height:123px}
  .ribbon--blurb .ribbon__text{padding:0 58px;font-size:16px;font-weight:700;line-height:1.25}

  .blurb{position:absolute;left:40px;right:40px;top:764px;color:var(--ink-white);text-align:center;font-size:19px;line-height:1.4}
  .divider{position:absolute;left:60px;right:60px;top:930px;border-top:1px solid var(--rule)}

  .brand-foot{position:absolute;left:0;right:0;top:962px;display:flex;align-items:center;justify-content:center;gap:10px}
  .brand-foot .brand-name{color:var(--ink-white);font-size:30px}
  .brand-foot .brand-mark{background:var(--ink-white);width:18px;height:18px}

  .web{position:absolute;left:0;right:0;top:1066px;text-align:center;color:var(--ink-white);font-size:25px}
  .web b{font-weight:800}
</style>
</head>
<body>

<section class="flyer-side flyer-side--front">
  <div class="scene-art" role="img" aria-label="Sepia street scene of old city buildings and a lone woman walking, framed inside a profile silhouette of a head"></div>

  <div class="brand-box"><span class="brand-mark"></span><span class="brand-name">PALE LANTERN</span></div>

  <p class="quote quote--front">
    <span class="line"><span class="mark">“</span> I have</span>
    <span class="line"><span class="big">Killed</span> my wife;</span>
    <span class="line">I'm glad</span>
    <span class="line">she's <span class="big">dead.</span><span class="mark">”</span></span>
  </p>

  <h1 class="tour-title">
    <span class="tour-title__place">HARBOURSIDE</span>
    <span class="tour-title__name">HIDDEN LANES</span>
  </h1>

  <div class="ribbon ribbon--walk">
    <svg viewBox="0 0 406 40" preserveAspectRatio="none" aria-hidden="true">
      <polygon points="0,0 406,0 394,20 406,40 0,40 12,20" fill="var(--ribbon)"/>
    </svg>
    <div class="ribbon__text">WALK</div>
  </div>

  <div class="ribbon ribbon--offer">
    <svg viewBox="0 0 293 85" preserveAspectRatio="none" aria-hidden="true">
      <polygon points="0,20 20,28 20,78 0,70 10,45" fill="var(--ribbon-dark)"/>
      <polygon points="293,20 273,28 273,78 293,70 283,45" fill="var(--ribbon-dark)"/>
      <path d="M20,12 Q146,0 273,12 L273,74 Q146,62 20,74 Z" fill="var(--ribbon)"/>
    </svg>
    <div class="ribbon__text">
      <span class="offer-amount">25% Discount</span>
      <span class="offer-code">Offer Codeword WICK</span>
    </div>
  </div>

  <p class="web">www.<b>palelantern</b>.com.au</p>
</section>

<section class="flyer-side flyer-side--back">
  <div class="scene-art" role="img" aria-label="Sepia photograph of two young children from the past, framed inside a profile silhouette of a head"></div>

  <p class="quote quote--back">
    <span class="line"><span class="mark">“</span> She's a</span>
    <span class="line"><span class="big">Beautiful</span> child',</span>
    <span class="line">isn't she? She's</span>
    <span class="line">the <span class="big">cause</span> of all</span>
    <span class="line">the <span class="big">trouble.</span> <span class="mark">”</span></span>
  </p>

  <div class="ribbon ribbon--blurb">
    <svg viewBox="0 0 400 123" preserveAspectRatio="none" aria-hidden="true">
      <polygon points="0,30 30,40 30,112 0,100 14,66" fill="var(--ribbon-dark)"/>
      <polygon points="400,30 370,40 370,112 400,100 386,66" fill="var(--ribbon-dark)"/>
      <path d="M30,18 Q200,4 370,18 L370,108 Q200,94 30,108 Z" fill="var(--ribbon)"/>
    </svg>
    <div class="ribbon__text">Pale lantern brings back Newcastle's hidden past, the forgotten past, the dark past that may not want to be remembered.</div>
  </div>

  <p class="blurb">Real stories from the streets around you. Discover the histories you won't hear anywhere else. The forgotten stories of yesteryear finally get a chance to be told. Through you they get to live again.</p>

  <div class="divider"></div>

  <div class="brand-foot"><span class="brand-mark"></span><span class="brand-name">PALE LANTERN</span></div>

  <p class="web">www.<b>palelantern</b>.com.au</p>
</section>

</body>
</html>
```